New Flyer Design Project

We need a flyer for our upcoming Rising Builders Forum.

5th Annual Rising Builders Forum
by the Council for Stewardship of Built Ventures (C-SBuV)
Theme: Step Forward
Date: January 24, 2020
Location: Bluestone Lodge Hotel and Conference Center, San Marcos, TX
#StepForward

This is event is put together by C-SBuV's Rising Builders Ring of Merit. I have a logo for the Ring of Merit, but not something that indicates it's the Rising Builders Ring.

More about the Forum (please don't include on the flyer): This Forum provides a venue to openly discuss issues affecting women in our industry and ideas and strategies to address those issues.

Architecture, Construction and Engineering are all struggling with a tremendous shortage of skilled talent. It is more important than ever for organizations to be able to attract, support and retain a talented workforce and to encourage more women to pursue and build vibrant careers in architecture, engineering and construction. Unfortunately, their attrition rate also remains high in these industries. Developing and retaining a skilled workforce includes identifying and addressing the specific needs of women in our industry. Man or Woman; Male or Female Brain, C-SBuV’s Rising Builders Forum will give you and your team the tools you need to excel as an Employer of Choice and a roadmap for individual continued career planning and success .

This unique Forum provides a venue to engage everyone from executives to those just beginning their careers with active, hands-on sessions and vibrant networking with the best and brightest in the A/E/C industry. In our usual C-SBuV Forum style, Keynotes become table participants and table participants become presenters, encouraging participants to assimilate what they are learning. Join local, state and national leaders and subject matter experts as we candidly explore and address the issues affecting women in our industry .

```html
<!DOCTYPE html>
<html lang="en">
<head>
<meta charset="utf-8">
<title>5th Annual Rising Builders Forum</title>
<link href="https://fonts.googleapis.com/css2?family=Archivo+Black&family=Barlow+Condensed:wght@700&family=Montserrat:wght@400;600&display=swap" rel="stylesheet">
<style>
  :root {
    --backdrop: #b9b9b9;
    --paper: #f4f4f4;
    --ink: #141414;
    --band: rgba(24, 24, 24, 0.9);
    --white: #ffffff;
    --accent-red: #e0202a;
    --brand-blue: #2a4f9e;
    --brand-green: #7fae3c;
    --grey-text: #555555;
  }
  * { box-sizing: border-box; margin: 0; padding: 0; }
  html, body {
    width: 1200px; height: 960px; overflow: hidden;
    background: var(--backdrop);
  }
  .flyer {
    position: absolute; left: 275px; top: 20px;
    width: 650px; height: 920px;
    background: linear-gradient(160deg, #ffffff 0%, var(--paper) 55%, #e2e2e2 100%);
    overflow: hidden;
    box-shadow: 0 10px 30px rgba(0,0,0,0.25);
  }
  .site-photo {
    position: absolute; inset: 0;
    clip-path: polygon(48% 0, 100% 0, 100% 100%, 40% 100%, 22% 62%);
    background:
      radial-gradient(ellipse at 80% 45%, rgba(90,130,170,0.55) 0%, rgba(90,130,170,0) 40%),
      linear-gradient(170deg, #3b2a1c 0%, #8a5a25 25%, #e08a25 45%, #b86a22 60%, #7b6f66 80%, #a9a9a9 100%);
  }
  .brand {
    position: absolute; left: 40px; top: 44px;
    display: flex; align-items: center; gap: 14px;
  }
  .brand-dot {
    width: 58px; height: 58px; border-radius: 50%;
    background: var(--brand-blue);
  }
  .brand-name {
    font-family: "Montserrat", sans-serif; font-weight: 600;
    font-size: 42px; color: #4a4a4a; letter-spacing: 1px;
  }
  .hashtag {
    position: absolute; right: 36px; top: 52px;
    font-family: "Archivo Black", sans-serif;
    font-size: 36px; color: var(--accent-red);
  }
  .headline {
    position: absolute; left: 40px; top: 150px;
    font-family: "Archivo Black", sans-serif; color: var(--ink);
    line-height: 0.95; text-transform: uppercase;
  }
  .headline .ordinal { font-size: 78px; display: block; }
  .headline .ordinal sup { font-size: 40px; vertical-align: 28px; }
  .headline .line { font-size: 58px; display: block; }
  .byline {
    position: absolute; left: 40px; top: 408px; width: 480px;
    font-family: "Montserrat", sans-serif; font-weight: 400;
    font-size: 17px; color: var(--ink);
    background: rgba(255,255,255,0.85); padding: 4px 8px;
  }
  .detail {
    position: absolute; left: 40px;
    background: var(--band); color: var(--white);
    font-family: "Barlow Condensed", sans-serif; font-weight: 700;
    padding: 10px 22px;
  }
  .detail-theme { top: 470px; width: 400px; font-size: 40px; }
  .detail-date { top: 548px; width: 430px; font-size: 40px; }
  .detail-location { top: 626px; width: 430px; font-size: 30px; line-height: 1.15; text-align: center; }
  .partner {
    position: absolute; right: 40px; bottom: 48px;
    display: flex; align-items: center; gap: 14px;
  }
  .partner-dot {
    width: 64px; height: 64px; border-radius: 50%;
    background: var(--brand-green);
  }
  .partner-name {
    font-family: "Montserrat", sans-serif; font-weight: 600;
    font-size: 38px; color: #4a4a4a;
  }
</style>
</head>
<body>
  <main class="flyer">
    <div class="site-photo" role="img" aria-label="Construction site steel framework in warm orange light with a smiling woman in a red hard hat and work gloves giving a thumbs up"></div>

    <div class="brand">
      <span class="brand-dot"></span>
      <span class="brand-name">C-SBuV</span>
    </div>

    <div class="hashtag">#StepForward</div>

    <h1 class="headline">
      <span class="ordinal">5<sup>th</sup></span>
      <span class="line">Annual Rising</span>
      <span class="line">Builders Forum</span>
    </h1>

    <p class="byline">by the Council for Stewardship of Built Ventures (C-SBuV)</p>

    <div class="detail detail-theme">Theme: Step Forward</div>
    <div class="detail detail-date">Date: January 24, 2020</div>
    <div class="detail detail-location">Location: Bluestone Lodge Hotel<br>and Conference Center,<br>San Marcos, TX</div>

    <div class="partner">
      <span class="partner-dot"></span>
      <span class="partner-name">Ring of Merit</span>
    </div>
  </main>
</body>
</html>
```